I need a Label design for my tavin 58 kombucha brand that is launching soon

I want a label to go on my tavin 58 kombucha bottle.
I have a logo image uploaded in the files but I am open to changes to this logo or even a completely New one if you think you can do better. This logo is based on the idea of an s-shaped naga. I particularly like the nagas from temples in luang prabang.
I also want to include the slogan - brewed to be bright.
The label should be some kind of oval at 80mm high by 70mm wide.
The label will go on a clear glass bottle. The kombucha will be visible and comes in different shades of red,yellow and purple.
The word kombucha should be clearly visible.
i want a very colorful, playful label. I'm very keen to see your ideas and I want something original.
Fermented foods and beverages

```html
<!DOCTYPE html>
<html lang="en">
<head>
<meta charset="utf-8">
<title>tavin 58 kombucha labels</title>
<link href="https://fonts.googleapis.com/css2?family=Bebas+Neue&family=Montserrat:wght@300;400&family=Satisfy&display=swap" rel="stylesheet">
<style>
  :root {
    --paper: #ffffff;
    --ink-light: #ffffff;

    --ginger-top: #f7961d;
    --ginger-ring: #c2680b;
    --ginger-band: #703f06;
    --ginger-accent: #f7961d;

    --rasp-top: #f2148f;
    --rasp-ring: #c9137b;
    --rasp-band: #6b0040;
    --rasp-accent: #f2148f;

    --orig-top: #bfe200;
    --orig-ring: #86c81a;
    --orig-band: #1f3a08;
    --orig-accent: #bfe200;
  }

  * { box-sizing: border-box; margin: 0; padding: 0; }

  html, body {
    width: 800px;
    height: 1200px;
    overflow: hidden;
    background: var(--paper);
  }

  .label-range {
    width: 800px;
    height: 1200px;
    display: flex;
    justify-content: center;
    align-items: center;
    gap: 20px;
  }

  .label {
    --top: var(--ginger-top);
    --ring: var(--ginger-ring);
    --band: var(--ginger-band);
    --accent: var(--ginger-accent);
    position: relative;
    flex: 0 0 236px;
    width: 236px;
    height: 300px;
    border-radius: 50%;
    border: 8px solid var(--ring);
    background: var(--top);
    overflow: hidden;
    text-align: center;
  }

  .label--raspberry {
    --top: var(--rasp-top);
    --ring: var(--rasp-ring);
    --band: var(--rasp-band);
    --accent: var(--rasp-accent);
  }

  .label--original {
    --top: var(--orig-top);
    --ring: var(--orig-ring);
    --band: var(--orig-band);
    --accent: var(--orig-accent);
  }

  .brand {
    position: absolute;
    top: 20px;
    left: 0;
    right: 0;
    display: flex;
    flex-direction: column;
    align-items: center;
  }

  .brand__dot {
    width: 46px;
    height: 46px;
    border-radius: 50%;
    background: var(--band);
  }

  .brand__name {
    margin-top: 12px;
    font-family: "Montserrat", sans-serif;
    font-weight: 300;
    font-size: 38px;
    line-height: 1;
    letter-spacing: -1px;
    white-space: nowrap;
    color: var(--ink-light);
  }

  .info-band {
    position: absolute;
    top: 155px;
    left: 0;
    right: 0;
    bottom: 0;
    background: var(--band);
    display: flex;
    flex-direction: column;
    align-items: center;
    padding-top: 10px;
  }

  .info-band__product {
    font-family: "Bebas Neue", sans-serif;
    font-size: 44px;
    line-height: 0.9;
    letter-spacing: 1px;
    color: var(--accent);
  }

  .info-band__slogan {
    font-family: "Satisfy", cursive;
    font-size: 17px;
    line-height: 1.15;
    white-space: nowrap;
    color: var(--ink-light);
  }

  .info-band__flavour {
    margin-top: 8px;
    font-family: "Montserrat", sans-serif;
    font-weight: 300;
    font-size: 12px;
    line-height: 1.25;
    letter-spacing: 0.5px;
    color: var(--ink-light);
    opacity: 0.85;
  }

  .info-band__icon {
    margin-top: 4px;
    width: 22px;
    height: 20px;
    border-radius: 50%;
    background: var(--accent);
  }
</style>
</head>
<body>
  <main class="label-range">

    <article class="label label--ginger">
      <div class="brand">
        <span class="brand__dot"></span>
        <span class="brand__name">tavin 58</span>
      </div>
      <div class="info-band">
        <span class="info-band__product">KOMBUCHA</span>
        <span class="info-band__slogan">brewed to be bright</span>
        <span class="info-band__flavour">GINGER</span>
        <span class="info-band__icon" role="img" aria-label="Ginger root icon"></span>
      </div>
    </article>

    <article class="label label--raspberry">
      <div class="brand">
        <span class="brand__dot"></span>
        <span class="brand__name">tavin 58</span>
      </div>
      <div class="info-band">
        <span class="info-band__product">KOMBUCHA</span>
        <span class="info-band__slogan">brewed to be bright</span>
        <span class="info-band__flavour">RASPBERRY</span>
        <span class="info-band__icon" role="img" aria-label="Raspberry icon"></span>
      </div>
    </article>

    <article class="label label--original">
      <div class="brand">
        <span class="brand__dot"></span>
        <span class="brand__name">tavin 58</span>
      </div>
      <div class="info-band">
        <span class="info-band__product">KOMBUCHA</span>
        <span class="info-band__slogan">brewed to be bright</span>
        <span class="info-band__flavour">ORIGINAL</span>
        <span class="info-band__icon" role="img" aria-label="Tea leaf icon"></span>
      </div>
    </article>

  </main>
</body>
</html>
```